Bright and beautiful business card for a coach

I'm a personal and business coach based in Perth, Australia. I need a business card that whilst subtle and elegant, will stand out and appeal on a table full of cards.

My business name is Tide Mentoring and the business card must represent the warmth and brightness implied in the name, without being gimmicky. It must have a warmth and appeal and be easy to read.

I prefer clean, minimalist designs.

It must align with the feel of my website and socials: https://www.tidementoring.com.au/
https://www.instagram.com/tidementoringau/
https://www.facebook.com/tidementoringau
Updates

Hi Designers Thank you so much for taking the time to submit designs. I wonder if I could have explained myself a little better. Most of the designs that have been submitted look rather formal and many have quite corporate looking embellishments on them (to my eye). I would like softer, warmer, more organic. I’m open to people playing about and being more abstract, using softer embellishments (e.g the line drawing flowers and grasses I’ve used in my socials) incorporating other colours from my palette or like the social icons in my email signature (in PDF), perhaps playing with size/oversize, playing with the bleed. Please don’t be constrained by what I’ve already done, it merely needs to compliment. I’m sorry if I’m not using the right words or have led you astray. I’m no designer, but I’ve done my website, socials, email signature etc all myself (my logo was a design contest) and I was really hoping for my business card to be something more creative than I could have made with a template. Reminder: No black cards/sides please. Thank you 😊

Target Market(s)

Individuals, most likely but not all female. Creative thinkers. Likely professionals.

Industry/Entity Type

Business & Personal Coach

Contact Information for Business Card

(Tide Mentoring Logo) Name: Maren Delsby; Title: Business & Personal Coach; Phone number: +61 (0)438 915307; Email: maren@tidementoring.com.au; Website: https://tidementoring.com.au; Social icons for Facebook, Instagram & LinkedIn: @tidementoringAU. Optional strapline: "A thinking partner to help you cut through the noise"

Font styles to use
Sans Serif

Colors
00AB8E
00BBA5
67D7C9
C6EFE9
E9F9F6
59FF00
82FF00
B8FF75
E3FFCB
F4FFEA
FFC000
F8CF3A
FAE287
FDF2CF
FEFAEE

Requirements
Must have
• Must align with feel of my website and socials. Must have a pop of #FFC000 (possibly whole of one side, or at least a block). Bright or white background. Easy to read.
Nice to have
• Possibly incorporate the sunshine/grass picture I have used in website and socials - will upload.
Should not have
• Must not be black or dark. Not impersonal or corporate looking.

```html
<!DOCTYPE html>
<html lang="en">
<head>
<meta charset="utf-8">
<title>Maren Delsby — Tide Mentoring Business Card</title>
<link rel="stylesheet" href="https://fonts.googleapis.com/css2?family=Lato:wght@400;700&display=swap">
<style>
  :root {
    --sun-gold: #FFC000;
    --icon-lime: #C9D13E;
    --icon-teal: #74B4C4;
    --text-white: #FFFFFF;
  }
  * { margin: 0; padding: 0; box-sizing: border-box; }
  html, body {
    width: 1200px;
    height: 686px;
    overflow: hidden;
    background: #ffffff;
  }
  .card {
    position: relative;
    width: 1200px;
    height: 686px;
    overflow: hidden;
    font-family: "Lato", sans-serif;
    color: var(--text-white);
  }
  .card__photo {
    position: absolute;
    inset: 0;
    background:
      radial-gradient(circle at 78% 2%, rgba(255, 250, 230, 0.95) 0%, rgba(250, 236, 190, 0.6) 10%, rgba(230, 215, 150, 0.18) 24%, rgba(0, 0, 0, 0) 38%),
      radial-gradient(ellipse at 20% 20%, rgba(60, 85, 30, 0.9) 0%, rgba(0, 0, 0, 0) 60%),
      linear-gradient(180deg, #5A7630 0%, #76933A 40%, #86A538 60%, #6A8A28 82%, #4F6E1E 100%);
  }
  .card__brand {
    position: absolute;
    left: 760px;
    top: 246px;
    display: flex;
    align-items: center;
  }
  .card__brand-dot {
    width: 26px;
    height: 26px;
    border-radius: 50%;
    background: var(--sun-gold);
    margin-right: 16px;
  }
  .card__brand-name {
    font-size: 40px;
    font-weight: 400;
    letter-spacing: 2px;
    line-height: 1;
    color: var(--text-white);
  }
  .card__name {
    position: absolute;
    left: 124px;
    top: 118px;
    font-size: 72px;
    font-weight: 700;
    line-height: 1;
    letter-spacing: 0.5px;
  }
  .card__title {
    position: absolute;
    left: 126px;
    top: 196px;
    font-size: 31px;
    font-weight: 700;
    line-height: 1;
  }
  .card__contacts {
    position: absolute;
    left: 124px;
    top: 285px;
    list-style: none;
    font-size: 33px;
    font-weight: 400;
    line-height: 47.5px;
  }
  .card__social {
    position: absolute;
    left: 131px;
    top: 471px;
    display: flex;
    align-items: center;
  }
  .social-dot {
    width: 54px;
    height: 54px;
    border-radius: 50%;
    margin-right: 13px;
  }
  .social-dot--gold { background: var(--sun-gold); }
  .social-dot--lime { background: var(--icon-lime); }
  .social-dot--teal { background: var(--icon-teal); }
  .card__handle {
    margin-left: 2px;
    font-size: 25px;
    font-weight: 700;
  }
  .card__strapline {
    position: absolute;
    left: 0;
    top: 574px;
    width: 1200px;
    height: 68px;
    background: var(--sun-gold);
    display: flex;
    align-items: center;
    justify-content: center;
    font-size: 34px;
    font-weight: 400;
  }
</style>
</head>
<body>
  <div class="card">
    <div class="card__photo" role="img" aria-label="Photograph of sunlit green grass with bright sunshine glowing through trees at the top right"></div>

    <div class="card__brand">
      <span class="card__brand-dot" aria-hidden="true"></span>
      <span class="card__brand-name">Tide Mentoring</span>
    </div>

    <h1 class="card__name">Maren Delsby</h1>
    <p class="card__title">Business &amp; Personal Coach</p>

    <ul class="card__contacts">
      <li>maren@tidementoring.com.au</li>
      <li>tidementoring.com.au</li>
      <li>+61 (0)438 915307</li>
    </ul>

    <div class="card__social">
      <span class="social-dot social-dot--gold" aria-hidden="true"></span>
      <span class="social-dot social-dot--lime" aria-hidden="true"></span>
      <span class="social-dot social-dot--teal" aria-hidden="true"></span>
      <span class="card__handle">@TideMentoringAU</span>
    </div>

    <div class="card__strapline">A thinking partner to help you cut through the noise</div>
  </div>
</body>
</html>
```